Flyer for Custom Home Builder!

my company is Harlow Ridge Homes, I am looking for a flyer that we can send via email to a customer, or print and hand out. I am thinking four pages so we could print this and fold it., possibly creating a folder. The name of the company is Harlow Ridge Homes our website is here www.harlowridgehomes-example.com. Some text you can use "Crafting luxury homes isn't just a job, it's our passion.
With meticulous attention to detail and an unwavering commitment to using the finest materials, Harlow Ridge Homes consistently delivers exceptional results that stand as a testament to our commitment to quality."

"Trust is the cornerstone of our foundation.
With a proven track record of delivering on our promises for over 16 years, we prioritize transparent communication and integrity throughout every step of the home-building journey".

you may need to obtain the photos here
https://files.example-share.net/f/k27pw4m8zrt03xq61bnv/h?key=48vn2c9q1x7mb5t0ekd3h&dl=0

Target Market(s)

We build homes for every wealthy clients, therefore the photos are extremely important

Industry/Entity Type

Construction.

Requirements
Must have
• clear larger photos

```html
<!DOCTYPE html>
<html lang="en">
<head>
<meta charset="utf-8">
<title>Harlow Ridge Homes – Four Page Flyer</title>
<link href="https://fonts.googleapis.com/css2?family=Montserrat:wght@400;500;600;700;800&family=Oswald:wght@500;600&display=swap" rel="stylesheet">
<style>
  :root{
    --canvas:#f1f1f1;
    --paper:#ffffff;
    --ink:#2b2b2b;
    --charcoal:#3a3a3a;
    --slate:#5b5b5b;
    --mid-gray:#8a8a8a;
    --light-gray:#c9c9c9;
    --pale-gray:#e4e4e4;
    --text-soft:#6f6f6f;
  }
  *{box-sizing:border-box;margin:0;padding:0}
  html,body{width:839px;height:1200px;overflow:hidden;background:var(--canvas)}
  body{position:relative;font-family:"Montserrat",sans-serif;color:var(--ink)}
  .page{position:absolute;width:350px;height:500px;background:var(--paper);overflow:hidden;box-shadow:0 1px 4px rgba(0,0,0,.12)}
  .page--portfolio{left:60px;top:84px}
  .page--cover{left:428px;top:84px}
  .page--about{left:60px;top:606px}
  .page--back{left:428px;top:606px}
  .photo{position:absolute;display:block}
  .section-tab{position:absolute;left:0;top:22px;background:var(--charcoal);color:#fff;font-weight:600;font-size:12px;letter-spacing:4px;padding:6px 16px 6px 24px}
  .brand{position:absolute;font-family:"Montserrat",sans-serif;font-weight:800;letter-spacing:2px;text-transform:uppercase;white-space:nowrap}
  .website{position:absolute;font-size:8px;font-weight:600;letter-spacing:.5px;text-transform:uppercase}
  /* portfolio */
  .city{position:absolute;font-weight:500;font-size:13px;letter-spacing:3px;color:var(--ink);text-align:center;line-height:1.15}
  .contact{position:absolute;display:flex;align-items:center;gap:5px;font-size:5.5px;color:var(--text-soft);line-height:1.35}
  .contact svg{flex:none}
  /* cover */
  .cover-title{position:absolute;left:0;right:0;text-align:center;color:#fff}
  .cover-title .premium{font-family:"Oswald",sans-serif;font-weight:600;font-size:40px;letter-spacing:2px;display:block}
  .cover-title .custom{display:inline-block;background:#fff;color:var(--ink);font-size:17px;font-weight:500;letter-spacing:2px;padding:2px 22px;margin:2px 0 4px}
  .cover-title .builder{font-family:"Oswald",sans-serif;font-weight:500;font-size:28px;letter-spacing:1px;display:block}
  /* about */
  .about-lead{position:absolute;left:22px;top:62px;width:300px;font-weight:700;font-size:9px;line-height:1.35;color:var(--ink)}
  .about-body{position:absolute;left:22px;top:108px;width:305px;font-size:5.5px;line-height:1.5;color:var(--text-soft)}
  .why{position:absolute;left:190px;top:200px;width:140px;text-align:center}
  .why h3{font-size:10px;font-weight:800;letter-spacing:1px}
  .why h4{font-size:9px;font-weight:700;margin-top:2px}
  .why ul{list-style:none;text-align:left;margin-top:10px}
  .why li{position:relative;padding-left:9px;font-size:5.5px;line-height:1.45;color:var(--text-soft);margin-bottom:7px}
  .why li::before{content:"";position:absolute;left:0;top:2px;width:4px;height:4px;background:var(--charcoal)}
  .service{position:absolute;left:190px;width:140px;background:var(--charcoal);color:#fff;font-size:8px;font-weight:600;letter-spacing:1px;text-align:center;padding:7px 4px}
</style>
</head>
<body>

<!-- Page 1: Portfolio -->
<section class="page page--portfolio">
  <div class="section-tab">PORTFOLIO</div>
  <svg class="photo" style="left:22px;top:55px" width="148" height="92" role="img" aria-label="Photo of a modern two-storey home in Austin">
    <defs><linearGradient id="p1" x1="0" y1="0" x2="0" y2="1"><stop offset="0" stop-color="#9cc0e0"/><stop offset=".6" stop-color="#d9d3c7"/><stop offset="1" stop-color="#6f7f5a"/></linearGradient></defs>
    <rect width="148" height="92" fill="url(#p1)"/>
  </svg>
  <svg class="photo" style="left:180px;top:55px" width="148" height="92" role="img" aria-label="Photo of a coastal home in Port Aransas">
    <defs><linearGradient id="p2" x1="0" y1="0" x2="0" y2="1"><stop offset="0" stop-color="#8fb8dc"/><stop offset=".6" stop-color="#e4e0d6"/><stop offset="1" stop-color="#7d8e62"/></linearGradient></defs>
    <rect width="148" height="92" fill="url(#p2)"/>
  </svg>
  <div class="city" style="left:22px;top:165px;width:148px">AUSTIN</div>
  <div class="city" style="left:180px;top:155px;width:148px">PORT<br>ARANSAS</div>
  <svg class="photo" style="left:22px;top:198px" width="148" height="86" role="img" aria-label="Photo of a bright open-plan kitchen interior">
    <defs><linearGradient id="p3" x1="0" y1="0" x2="1" y2="1"><stop offset="0" stop-color="#f2efe8"/><stop offset="1" stop-color="#b9ab95"/></linearGradient></defs>
    <rect width="148" height="86" fill="url(#p3)"/>
  </svg>
  <svg class="photo" style="left:180px;top:198px" width="148" height="86" role="img" aria-label="Photo of a living room with large windows">
    <defs><linearGradient id="p4" x1="0" y1="0" x2="1" y2="1"><stop offset="0" stop-color="#eae6de"/><stop offset="1" stop-color="#a89c86"/></linearGradient></defs>
    <rect width="148" height="86" fill="url(#p4)"/>
  </svg>
  <svg class="photo" style="left:0;top:296px" width="350" height="90" aria-hidden="true">
    <polygon points="0,0 350,0 350,60 300,90 0,90" fill="var(--slate)"/>
    <polygon points="300,90 350,60 350,90" fill="var(--light-gray)"/>
  </svg>
  <div class="brand" style="left:22px;top:330px;font-size:15px;color:#fff">HARLOW RIDGE HOMES</div>
  <div class="contact" style="left:22px;top:405px">
    <svg width="12" height="12" viewBox="0 0 12 12"><circle cx="6" cy="6" r="5.5" fill="none" stroke="var(--mid-gray)"/><path d="M4 3.5l1.2 0 .5 1.5-.8.6a4 4 0 0 0 1.6 1.6l.6-.8 1.5.5v1.2c-2.8.3-5-1.9-4.6-4.6z" fill="var(--mid-gray)"/></svg>
    <span>Call us today<br>(512) 555-0148</span>
  </div>
  <div class="contact" style="left:180px;top:405px">
    <svg width="12" height="12" viewBox="0 0 12 12"><circle cx="6" cy="6" r="5.5" fill="none" stroke="var(--mid-gray)"/><rect x="3" y="4" width="6" height="4" fill="none" stroke="var(--mid-gray)" stroke-width=".8"/><path d="M3 4l3 2.2L9 4" fill="none" stroke="var(--mid-gray)" stroke-width=".8"/></svg>
    <span>Email us<br>info@harlowridge.example</span>
  </div>
  <div class="contact" style="left:22px;top:432px">
    <svg width="12" height="12" viewBox="0 0 12 12"><circle cx="6" cy="6" r="5.5" fill="none" stroke="var(--mid-gray)"/><path d="M6 2.8a2 2 0 0 1 2 2c0 1.5-2 4-2 4s-2-2.5-2-4a2 2 0 0 1 2-2z" fill="var(--mid-gray)"/></svg>
    <span>Location<br>482 Lakeview Terrace, Suite 210</span>
  </div>
  <div class="website" style="right:22px;top:470px;color:var(--ink)">www.harlowridgehomes-example.com</div>
</section>

<!-- Page 2: Cover -->
<section class="page page--cover">
  <div class="brand" style="left:22px;top:26px;font-size:16px;color:var(--ink)">HARLOW RIDGE HOMES</div>
  <svg class="photo" style="left:0;top:60px" width="350" height="215" role="img" aria-label="Photo of a luxury modern home with a pool at dusk">
    <defs><linearGradient id="c1" x1="0" y1="0" x2="0" y2="1"><stop offset="0" stop-color="#b7cfe3"/><stop offset=".5" stop-color="#d8d6d0"/><stop offset=".8" stop-color="#7fb4c6"/><stop offset="1" stop-color="#4f8aa0"/></linearGradient></defs>
    <polygon points="80,0 350,0 350,215 0,215 0,60" fill="url(#c1)"/>
  </svg>
  <svg class="photo" style="left:0;top:265px" width="350" height="235" aria-hidden="true">
    <polygon points="0,18 350,0 350,200 0,200" fill="var(--slate)"/>
    <polygon points="0,200 350,200 350,235 0,235" fill="var(--paper)"/>
    <polygon points="260,200 350,160 350,200" fill="var(--light-gray)"/>
  </svg>
  <div class="cover-title" style="top:300px">
    <span class="premium">PREMIUM</span>
    <span class="custom">Custom</span>
    <span class="builder">HOME BUILDER</span>
  </div>
  <div class="website" style="right:22px;top:476px;color:var(--ink)">www.harlowridgehomes-example.com</div>
</section>

<!-- Page 3: About -->
<section class="page page--about">
  <div class="section-tab">ABOUT US</div>
  <p class="about-lead">Harlow Ridge Homes is a premier custom home builder committed to creating exceptional, one-of-a-kind homes that reflect the unique vision and style of our clients.</p>
  <p class="about-body">With over sixteen years of experience in the industry, we have earned a reputation for unparalleled craftsmanship and attention to detail. Every home we build begins with listening closely to our clients, understanding how they live and what they value most. From the first sketch to the final walkthrough, our experienced team guides each project with care, honesty and clear communication, so every client feels confident and informed along the way.</p>
  <svg class="photo" style="left:22px;top:178px" width="155" height="88" role="img" aria-label="Photo of an interior staircase and hallway">
    <defs><linearGradient id="a1" x1="0" y1="0" x2="1" y2="1"><stop offset="0" stop-color="#f0ece4"/><stop offset="1" stop-color="#9b8d78"/></linearGradient></defs>
    <rect width="155" height="88" fill="url(#a1)"/>
  </svg>
  <svg class="photo" style="left:22px;top:272px" width="155" height="88" role="img" aria-label="Photo of a home exterior at sunset">
    <defs><linearGradient id="a2" x1="0" y1="0" x2="0" y2="1"><stop offset="0" stop-color="#c97a6a"/><stop offset=".5" stop-color="#9a86a6"/><stop offset="1" stop-color="#4d4a52"/></linearGradient></defs>
    <rect width="155" height="88" fill="url(#a2)"/>
  </svg>
  <svg class="photo" style="left:22px;top:366px" width="155" height="112" role="img" aria-label="Photo of a modern kitchen with an island">
    <defs><linearGradient id="a3" x1="0" y1="0" x2="1" y2="1"><stop offset="0" stop-color="#ebe8e2"/><stop offset="1" stop-color="#8e8a84"/></linearGradient></defs>
    <rect width="155" height="112" fill="url(#a3)"/>
  </svg>
  <div class="why">
    <h3>WHY</h3>
    <h4>Harlow Ridge Homes</h4>
    <ul>
      <li>Crafting luxury homes isn't just a job, it's our passion.</li>
      <li>With meticulous attention to detail and an unwavering commitment to using the finest materials, Harlow Ridge Homes consistently delivers exceptional results that stand as a testament to our commitment to quality.</li>
      <li>Trust is the cornerstone of our foundation.</li>
      <li>With a proven track record of delivering on our promises for over 16 years, we prioritize transparent communication and integrity throughout every step of the home-building journey.</li>
    </ul>
  </div>
  <div class="service" style="top:415px">DESIGN &amp; BUILD</div>
  <div class="service" style="top:446px">INTERIOR/EXTERIOR<br>REMODELS</div>
</section>

<!-- Page 4: Back cover -->
<section class="page page--back">
  <svg class="photo" style="left:0;top:0" width="350" height="400" role="img" aria-label="Photo of a glass-walled luxury home reflected in a pool at twilight">
    <defs><linearGradient id="b1" x1="0" y1="0" x2="0" y2="1"><stop offset="0" stop-color="#7fa6cf"/><stop offset=".45" stop-color="#c9cdd0"/><stop offset=".7" stop-color="#5c6f7e"/><stop offset="1" stop-color="#2f4658"/></linearGradient></defs>
    <polygon points="0,0 350,0 350,320 0,400" fill="url(#b1)"/>
  </svg>
  <svg class="photo" style="left:0;top:360px" width="350" height="140" aria-hidden="true">
    <polygon points="0,60 0,140 20,140 60,60" fill="var(--pale-gray)"/>
    <polygon points="30,140 70,60 95,60 55,140" fill="var(--light-gray)"/>
    <polygon points="65,140 105,60 118,60 78,140" fill="var(--pale-gray)"/>
  </svg>
  <div class="brand" style="right:22px;top:448px;font-size:16px;color:var(--ink)">HARLOW RIDGE HOMES</div>
</section>

</body>
</html>
```